Tasteful instructions for employees/guests to wash hands

Need an aesthetic visualisation of steps to wash hands.
While we would like to convey the proper steps to wash hands we also don't want to treat our staff/guests like children, rather provide a quick reminder.
Suggested sizes
16″ × 24″
11″ × 14″
A simplified version of these steps:
- Wet your hands with clean, running water (warm or cold), turn off the tap, and apply soap.
- Lather your hands by rubbing them together with the soap. Lather the backs of your hands, between your fingers, and under your nails.
- Scrub your hands for at least 20 seconds.
- Rinse your hands well under clean, running water.
- Dry your hands using a clean towel or air dry them.

```html
<!DOCTYPE html>
<html lang="en">
<head>
<meta charset="utf-8">
<title>Steps to Wash Hands</title>
<link href="https://fonts.googleapis.com/css2?family=Montserrat:wght@500;600;700;800&display=swap" rel="stylesheet">
<style>
  :root {
    --navy: #0d1a42;
    --panel: #dae6fb;
    --divider: #ffffff;
    --backdrop: #eef0f3;
    --ink: #0d1a42;
  }
  * { margin: 0; padding: 0; box-sizing: border-box; }
  html, body { width: 1029px; height: 1200px; overflow: hidden; background: var(--backdrop); }
  .poster {
    position: absolute; left: 42px; top: 0;
    width: 944px; height: 1200px;
    background: var(--panel);
    font-family: "Montserrat", sans-serif;
    color: var(--ink);
    overflow: hidden;
  }
  .header {
    position: absolute; left: 0; top: 0; width: 944px; height: 239px;
    background: var(--navy); color: #fff; text-align: center;
  }
  .header-kicker {
    position: absolute; left: 0; right: 0; top: 52px;
    font-size: 38px; font-weight: 800; letter-spacing: -0.4px; line-height: 1;
  }
  .header-title {
    position: absolute; left: 0; right: 0; top: 96px;
    font-size: 117px; font-weight: 800; letter-spacing: -3px; line-height: 1;
  }
  .footer-band {
    position: absolute; left: 0; bottom: 0; width: 944px; height: 33px; background: var(--navy);
  }
  .dividers, .dial { position: absolute; left: 0; top: 0; }
  .step-text {
    position: absolute; font-size: 22.5px; font-weight: 500; white-space: nowrap;
  }
  .step-dry { left: 61px; top: 281px; width: 360px; text-align: center; line-height: 32px; }
  .step-wet { left: 531px; top: 281px; width: 360px; text-align: center; line-height: 32px; }
  .step-lather { right: 47px; top: 671px; text-align: right; line-height: 28.6px; }
  .step-rinse { left: 46px; top: 671px; line-height: 28.6px; }
  .step-scrub { left: 263px; top: 1019px; line-height: 32px; }
  .step-number {
    position: absolute; font-size: 33px; font-weight: 800; line-height: 1;
    transform: translate(-50%, -50%);
  }
  .icon-slot { position: absolute; background: var(--navy); border-radius: 22px; }
</style>
</head>
<body>
<main class="poster">
  <header class="header">
    <div class="header-kicker">AN AESTHETIC VISUALISATION OF STEPS TO</div>
    <h1 class="header-title">WASH HANDS</h1>
  </header>

  <svg class="dividers" width="944" height="1200" viewBox="0 0 944 1200" aria-hidden="true">
    <g stroke="var(--divider)" stroke-width="3">
      <line x1="474" y1="239" x2="474" y2="484"/>
      <line x1="0" y1="651" x2="253" y2="651"/>
      <line x1="688" y1="651" x2="944" y2="651"/>
      <line x1="361" y1="904" x2="47" y2="1167"/>
      <line x1="580" y1="891" x2="877" y2="1167"/>
    </g>
  </svg>

  <svg class="dial" width="944" height="1200" viewBox="0 0 944 1200">
    <circle cx="472" cy="698" r="209" fill="none" stroke="var(--navy)" stroke-width="19" stroke-dasharray="2.6 10.53"/>
    <circle cx="472" cy="698" r="197" fill="var(--navy)" role="img" aria-label="Illustration of two hands being washed under a running tap"/>
    <g fill="var(--navy)">
      <path d="M630 538 l14 -4 l-6 12 z"/>
      <path d="M694 762 l-12 -8 l0 14 z"/>
      <path d="M472 928 l-7 -10 h14 z"/>
      <path d="M256 762 l12 -8 l0 14 z"/>
      <path d="M316 535 l-12 -3 l5 12 z"/>
    </g>
  </svg>

  <span class="step-number" style="left:644px;top:522px">1</span>
  <span class="step-number" style="left:712px;top:774px">2</span>
  <span class="step-number" style="left:476px;top:945px">3</span>
  <span class="step-number" style="left:234px;top:774px">4</span>
  <span class="step-number" style="left:306px;top:508px">5</span>

  <p class="step-text step-dry">Dry your hands using a clean<br>towel or air dry them.</p>
  <p class="step-text step-wet">Wet your hands with clean,<br>running water (warm or cold),<br>turn off the tap, and apply<br>soap.</p>
  <p class="step-text step-lather">Lather your<br>hands by<br>rubbing them<br>together with<br>the soap.<br>Lather the<br>backs<br>of your<br>hands,<br>between<br>your<br>fingers, &amp;<br>under your<br>nails.</p>
  <p class="step-text step-rinse">Rinse your<br>hands well<br>under<br>clean,<br>running<br>water.</p>
  <p class="step-text step-scrub">Scrub your hands<br>for at least<br>20 seconds.</p>

  <div class="icon-slot" style="left:91px;top:410px;width:143px;height:176px" role="img" aria-label="Icon of a hand drying on a towel"></div>
  <div class="icon-slot" style="left:703px;top:440px;width:178px;height:166px" role="img" aria-label="Icon of a soap dispenser above an open hand"></div>
  <div class="icon-slot" style="left:666px;top:825px;width:105px;height:120px" role="img" aria-label="Icon of hands rubbing together with droplets"></div>
  <div class="icon-slot" style="left:52px;top:850px;width:151px;height:197px" role="img" aria-label="Icon of soapy hands under a dripping tap"></div>
  <div class="icon-slot" style="left:502px;top:1002px;width:170px;height:127px" role="img" aria-label="Icon of a hand on a sparkling soap bar"></div>

  <div class="footer-band"></div>
</main>
</body>
</html>
```